Etiketten für Ätherische Öle, Extrakte und Speiseöle gesucht
Zielgruppe
Wir verkaufen natürlich Produkte. Ätherische öle, Extrakte, Speise öle.
Wir verkaufen im Webshop, Kaufwelt und auch im Betrieb.
https://www.natur-sefo.com
Wir verkaufen hauptsächlich innerhalb Italiens und Deutschland daher doppel sprachig.
Aufgabenstellung
Guten Tag
Bitte verwenden Sie! : * beispiel_10_ml_etikett_nachbau.jpg *
Da mir die kleinste Größe die wichtigste ist habe ich ein beispiel Hochgeladen. Das kleinste Etikett lässt sich öffnen und daher sind nur 7 cm ersichtlich und man muss das Etikett aufmachen.
Habe ein Beispiel Hochgeladen. Aber bitte einfach kreativ sein. *Anhang: beispiel Etikett*
Sobald ich eine Art vom kelinsten habe würde ich dies für die 2 anderen Größen übernehmen aber das man Sie irgendwie gut unterscheiden kann da dies dann komplett andere Produkte (Extrakte/Speise öl) sein werden.
Erstellung von drei unterschiedlichen Größen von Etiketten mit folgenden Eigenschaften:
Am wichtigsten ist mir das kleinste Etikett da dies auch am schwersten ist daher habe ich die anderen Größen nun gelöscht!
• 10 ml Länge: 155 mm Breite: 32 mm.
Brauche 3 unterschiedliche Grund Farben: z. B. Ätherische Öle (Grün) Extrakte (Rot) Speiseöle (gelb). Die Farben lasse ich sie entscheiden.
Die Etiketten müssen 2 Sprachen (Deutsch / Italienisch) sein deshalb muss dieses berücksichtigt werden.
Anbei finden Sie:
• Logo (Bild Logo)
• Beispiel Text ätherische Öle
• Bilder der aktuellen Flaschen
Unter https://www.natur-sefo.com/de finden Sie meine Seite
Anmerkung: Im Anhang: *Back*
Habe ich mein Logo mit Firmennamen ; Bio des Hollmer Tobias
Da ich jedoch nicht alle Produkte im biologischen Anbau habe und mein Logo zu miss Verständnis führen könnte habe ich ein Bildliches Logo gemacht das ich fortan auf meinen Produkten haben möchte. Im besonderes dieses Grün das in beiden vorhanden ist versuche ich zu integrieren.
Habe selbst ein Etikett designet das aber sehr unprofessionell wirkt aber dieses Grüne das ich gerne als merkmal unterbringen würde.
Siehe Anhang: neemöl

```html
<!DOCTYPE html>
<html lang="de">
<head>
<meta charset="utf-8">
<title>Lavanda Vera – Etikett 10 ml (155 × 32 mm)</title>
<link href="https://fonts.googleapis.com/css2?family=Inter:wght@400;600;700&family=Allura&display=swap" rel="stylesheet">
<style>
  :root {
    --page: #ffffff;
    --white: #ffffff;
    --wine: #8c0a10;
    --wine-deep: #7a0007;
    --blush: #f2d6d8;
    --brand-green: #4a9a3c;
    --ink-blue: #2b2f9c;
    --date-box: #d9b2b6;
  }
  html, body {
    margin: 0;
    width: 1200px;
    height: 466px;
    overflow: hidden;
    background: var(--page);
  }
  /* 155 × 32 mm → 1160 × 240 px */
  .label {
    position: absolute;
    left: 20px;
    top: 113px;
    width: 1160px;
    height: 240px;
    overflow: hidden;
    font-family: "Inter", sans-serif;
    background: linear-gradient(to bottom,
      var(--white) 0px, var(--white) 92px,
      var(--blush) 102px, var(--wine) 138px, var(--wine-deep) 240px);
  }
  .label__frame {
    position: absolute;
    inset: 5px;
    border: 2px solid var(--brand-green);
  }
  .label__green-strip {
    position: absolute;
    left: 0;
    right: 0;
    bottom: 0;
    height: 4px;
    background: var(--brand-green);
  }

  /* left column */
  .usage {
    position: absolute;
    left: 14px;
    top: 12px;
    width: 366px;
    display: grid;
    grid-template-columns: 1fr 1fr;
    column-gap: 12px;
    font-size: 9.4px;
    line-height: 11.2px;
    color: var(--ink-blue);
  }
  .usage p { margin: 0; }
  .usage strong { font-weight: 700; color: var(--brand-green); }
  .company {
    position: absolute;
    left: 16px;
    top: 127px;
    font-size: 9.8px;
    line-height: 11.2px;
    color: var(--white);
  }
  .company__title { font-weight: 700; }

  /* centre panel */
  .product-panel {
    position: absolute;
    left: 398px;
    top: 10px;
    width: 330px;
    height: 232px;
  }
  .product-panel__art {
    position: absolute;
    inset: 0;
    background:
      radial-gradient(circle at 50% 36%, rgba(190,150,230,0.85) 0, rgba(200,120,190,0.6) 55px, rgba(220,150,170,0.25) 110px, transparent 140px),
      linear-gradient(160deg, rgba(245,235,245,0.9) 0%, rgba(200,120,150,0.55) 55%, rgba(230,130,60,0.55) 80%, rgba(180,60,80,0.5) 100%);
  }
  .product-name {
    position: absolute;
    left: 0;
    right: 0;
    top: 80px;
    text-align: center;
    font-family: "Allura", cursive;
    font-size: 52px;
    line-height: 1;
    color: var(--white);
  }
  .product-variety {
    position: absolute;
    left: 0;
    right: 0;
    top: 136px;
    text-align: center;
    font-size: 14px;
    letter-spacing: 7px;
    color: var(--white);
  }
  .product-volume {
    position: absolute;
    left: 0;
    right: 0;
    top: 196px;
    text-align: center;
    font-size: 15px;
    color: var(--white);
  }

  /* right column */
  .warnings {
    position: absolute;
    left: 750px;
    top: 14px;
    width: 392px;
    display: grid;
    grid-template-columns: 1fr 1fr;
    column-gap: 12px;
    font-size: 10px;
    line-height: 12px;
    color: var(--ink-blue);
  }
  .warnings p { margin: 0; }
  .bottling {
    position: absolute;
    left: 752px;
    top: 124px;
    width: 390px;
    color: var(--white);
  }
  .bottling__country { font-size: 12px; margin: 0 0 4px; }
  .bottling__lot { font-size: 9px; font-weight: 600; margin: 0 0 7px; }
  .bottling__best { font-size: 8px; font-weight: 600; margin: 0 0 3px; }
  .bottling__date {
    width: 200px;
    height: 42px;
    background: var(--date-box);
    border-radius: 2px;
  }
</style>
</head>
<body>
<div class="label">
  <div class="label__green-strip"></div>
  <div class="label__frame"></div>

  <div class="usage">
    <div lang="de">
      <p>100% natürliches etherisches Öl. Aroma-Kosmetikum zur Körperpflege.</p>
      <p><strong>Anwendung:</strong> Als Haut- u. Massageöl max 15 Tr. Mit 50 ml z.B. Mandelöl mischen.</p>
      <p>Als Badezusatz 8-15 Tr. Auf 4 Eßl. Sahne oder Milch ins Badewasser geben.</p>
    </div>
    <div lang="it">
      <p>100% olio essenziale naturale. Cosmetico aromatico per la cura del corpo.</p>
      <p><strong>Uso:</strong> Olio per pelle e massaggi max 15 gocce in 50 ml p.es. olio di mandorle.</p>
      <p>Nel bagno 8-15 gocce in 4 cucchiai di panna o latte nell'acqua.</p>
    </div>
  </div>

  <div class="company">
    <div class="company__title">Firmenname / Ragione sociale:</div>
    <div>Bio des Hollmer Tobias</div>
    <div>Talweg 8</div>
    <div>I-39020 Marling</div>
    <div>IVA: IT04518260193</div>
    <div>CF.: HLLTBS88M12F132K</div>
    <div>Tel; +39 0473/218406 Handy; 3405127783</div>
    <div>https://www.natur-sefo.com/</div>
    <div>info.natursefo@postamail.it</div>
  </div>

  <div class="product-panel">
    <div class="product-panel__art" role="img" aria-label="Blütenfoto in Lila-, Rosa- und Orangetönen"></div>
    <div class="product-name">Lavanda</div>
    <div class="product-variety">Vera</div>
    <div class="product-volume">10 ml</div>
  </div>

  <div class="warnings">
    <p lang="de">Nur in der angegeben Verdünnung anwenden! Nicht in die Augen oder auf die Schleimhäute bringen! Außer Reichweite von Kindern lagern.</p>
    <p lang="it">Usare solo nella diluizione indicata! Non applicare negli occhi o sulle mucose! Tenere fuori dalla portata dei bambini.</p>
  </div>

  <div class="bottling">
    <p class="bottling__country">Abgefüllt in Italien / Imbottigliato in Italia</p>
    <p class="bottling__lot">LottoNummer/CH nummer · N. lotto: 123456</p>
    <p class="bottling__best">Mindestens haltbar bis / Da consumarsi preferibilmente entro:</p>
    <div class="bottling__date"></div>
  </div>
</div>
</body>
</html>
```